Business Card for a Jewellery Brand

Business card for an upscale jewellery brand. Attached is the brand logo and icon and color board. I am looking for two card versions: one for the founder and one is generic. The card should be elegant and convey upscale and premium feel. I am open to both square and rectangle card shapes.

Industry/Entity Type

Jewelry

Contact Information for Business Card

Two cards: (1) Sunila Perumbadi (Founder) (2) General
(1) Sunila Perumbadi card should have Name: Sunila Perumbadi, Title: Founder Email id: sunila@quelm.com.au. Phone no: +61412555307
(2) Generic card should have Email id: info@quelm.com.au. Phone no: +61431555962

Requirements
Must have
• Workmark
• ICON
• Phone no
• Email ID
• ABN: 48917205563 (Note: ABN is Business number in Australia)
• Website: www.quelm.com.au
• Instagram: quelm_jewellery
• Facebook: @quelmjewellery
Nice to have
• Tagline

```html
<!DOCTYPE html>
<html lang="en">
<head>
<meta charset="utf-8">
<title>QUELM Business Cards</title>
<link href="https://fonts.googleapis.com/css2?family=Open+Sans:wght@400;600&display=swap" rel="stylesheet">
<style>
  :root {
    --page: #ecebea;
    --card: #ffffff;
    --card-mist: #efefef;
    --panel-grey: #d4d4d4;
    --rose: #e8918b;
    --copper-light: #e3bcae;
    --copper-dark: #a77568;
    --ink: #1d1d1d;
  }
  * { margin: 0; padding: 0; box-sizing: border-box; }
  html, body { width: 1200px; height: 1200px; overflow: hidden; }
  body {
    background: var(--page);
    font-family: "Open Sans", Arial, sans-serif;
    position: relative;
  }
  .card {
    position: absolute;
    left: 250px;
    width: 700px;
    height: 400px;
    background: radial-gradient(ellipse at 60% 30%, var(--card-mist), var(--card) 70%);
    box-shadow: 0 6px 18px rgba(0,0,0,0.12);
    overflow: hidden;
  }
  .card--front { top: 150px; }
  .card--back { top: 650px; }

  /* Front */
  .product-photo {
    position: absolute;
    left: 0; top: 0;
    width: 250px; height: 400px;
    background: radial-gradient(ellipse at 50% 55%, var(--copper-light) 0%, #cdb8b1 30%, var(--panel-grey) 60%);
  }
  .divider {
    position: absolute;
    top: 0;
    left: 262px;
    width: 4px;
    height: 400px;
    background: var(--rose);
  }
  .wordmark {
    color: var(--rose);
    font-weight: 600;
    letter-spacing: 0.35em;
    display: flex;
    align-items: center;
    gap: 18px;
  }
  .wordmark__dot {
    width: 14px; height: 14px;
    border-radius: 50%;
    background: var(--rose);
  }
  .card--front .wordmark {
    position: absolute;
    left: 350px; top: 170px;
    font-size: 50px;
  }

  /* Back */
  .logo-panel {
    position: absolute;
    left: 0; top: 0;
    width: 300px; height: 400px;
    background: linear-gradient(160deg, #f6f6f6, #ececec);
    display: flex;
    align-items: center;
    justify-content: center;
  }
  .logo-panel .wordmark { font-size: 38px; gap: 12px; }
  .contact {
    position: absolute;
    left: 340px; top: 70px;
  }
  .contact__name {
    color: var(--rose);
    font-size: 27px;
    font-weight: 400;
    margin-bottom: 10px;
  }
  .contact__list { list-style: none; }
  .contact__item {
    display: flex;
    align-items: center;
    gap: 10px;
    font-size: 19px;
    color: var(--ink);
    line-height: 30px;
  }
  .contact__icon {
    width: 16px; height: 16px;
    flex: none;
  }
  .contact__icon--plain { background: var(--rose); border-radius: 2px; }
  .contact__icon--outline { border: 1.5px solid var(--rose); border-radius: 3px; }
  .contact__spacer { width: 16px; flex: none; }
</style>
</head>
<body>

<section class="card card--front">
  <div class="product-photo" role="img" aria-label="Photo of a pair of rose-gold dome drop earrings on a grey backdrop"></div>
  <div class="divider"></div>
  <div class="wordmark"><span class="wordmark__dot"></span>QUELM</div>
</section>

<section class="card card--back">
  <div class="logo-panel">
    <div class="wordmark"><span class="wordmark__dot"></span>QUELM</div>
  </div>
  <div class="contact">
    <h1 class="contact__name">Sunila Perumbadi</h1>
    <ul class="contact__list">
      <li class="contact__item"><span class="contact__spacer"></span>ABN: 48917205563</li>
      <li class="contact__item">
        <svg class="contact__icon" viewBox="0 0 16 16"><path d="M3 1.5l3 3-1.5 2c1 2 2.5 3.5 4.5 4.5l2-1.5 3 3-2 2C6 14 2 10 1.5 3.5z" fill="var(--rose)"/></svg>
        +61412555307
      </li>
      <li class="contact__item">
        <svg class="contact__icon" viewBox="0 0 16 16"><rect x="1" y="3" width="14" height="10" fill="none" stroke="var(--rose)" stroke-width="1.4"/><path d="M1 3l7 6 7-6" fill="none" stroke="var(--rose)" stroke-width="1.4"/></svg>
        sunila@quelm.com.au
      </li>
      <li class="contact__item">
        <svg class="contact__icon" viewBox="0 0 16 16"><circle cx="8" cy="8" r="6.5" fill="none" stroke="var(--rose)" stroke-width="1.3"/><ellipse cx="8" cy="8" rx="3" ry="6.5" fill="none" stroke="var(--rose)" stroke-width="1.1"/><path d="M1.5 8h13" stroke="var(--rose)" stroke-width="1.1"/></svg>
        quelm.com.au
      </li>
      <li class="contact__item"><span class="contact__icon contact__icon--outline"></span>quelm_jewellery</li>
      <li class="contact__item"><span class="contact__icon contact__icon--plain"></span>@quelmjewellery</li>
    </ul>
  </div>
</section>

</body>
</html>
```